New web page, 2 companies on the one page

A new web page for an engineering consultancy and maintenance management company

Corrick & Associates is the parent company covering the design and consultancy
Trivolt Engineering is the Maintenance and Reliability company

Target Market(s)

Food & Beverage, ingredients Manufacturing
engineering managers

Coding

Coded - Design and coding required

Number of Pages Required

1 page

Font styles to use
Other font styles liked:
• Roboto

Colors
1861ab
85acd3
d0dfed
cee9f5

```html
<!DOCTYPE html>
<html lang="en">
<head>
<meta charset="utf-8">
<title>Corrick &amp; Associates | Trivolt Engineering</title>
<link href="https://fonts.googleapis.com/css2?family=Audiowide&family=Roboto:wght@400;500;700&display=swap" rel="stylesheet">
<style>
:root{
  --blue:#00a9e0;
  --blue-dark:#1861ab;
  --blue-mid:#85acd3;
  --blue-pale:#d0dfed;
  --sky:#e6f4fb;
  --ink:#1f1b1f;
  --text:#222;
  --grey:#5a5a5a;
  --white:#fff;
}
*{margin:0;padding:0;box-sizing:border-box}
html,body{width:1200px;height:4246px;overflow:hidden}
body{position:relative;background:var(--white);font-family:"Roboto",sans-serif;color:var(--text)}
.abs{position:absolute}
.display{font-family:"Audiowide",sans-serif;text-transform:uppercase}

/* header */
.brand{left:173px;top:38px;display:flex;align-items:center;gap:14px}
.brand-mark{width:40px;height:40px;background:var(--blue)}
.brand-name{font-weight:700;font-size:30px;color:var(--ink)}
.nav{left:640px;top:60px;display:flex;gap:26px;font-size:14px;font-weight:500}
.nav a{color:var(--ink);text-decoration:none}
.nav a.active{color:var(--blue)}

/* hero */
.hero-art{left:0;top:0;width:1200px;height:1014px;
  background:
    radial-gradient(ellipse 230px 150px at 290px 600px,#ffffff 0%,#e4e8ee 55%,rgba(228,232,238,0) 100%),
    radial-gradient(ellipse 170px 140px at 720px 580px,#d9b27a 0%,#b98a52 55%,rgba(185,138,82,0) 100%),
    radial-gradient(ellipse 200px 120px at 960px 730px,#e9e6df 0%,rgba(233,230,223,0) 100%),
    radial-gradient(ellipse 150px 90px at 1110px 880px,#c23a3a 0%,rgba(60,50,50,.9) 45%,rgba(60,50,50,0) 100%),
    radial-gradient(ellipse 220px 80px at 720px 870px,#e7c458 0%,rgba(231,196,88,0) 100%),
    linear-gradient(180deg,#ffffff 0%,#f3f4f6 35%,#e2e4e7 55%,#cfc6b8 72%,#b09a7e 86%,#8e7a62 100%)}
.hero-title{left:0;width:1200px;top:195px;text-align:center;font-size:96px;color:var(--ink);line-height:1}
.hero-sub{left:0;width:1200px;top:298px;text-align:center;font-size:46px;color:var(--blue);letter-spacing:30px;padding-left:30px;line-height:1}

/* about */
.about-title{left:0;width:1200px;top:1138px;text-align:center;font-size:40px;color:var(--white)}
.about-copy{left:178px;width:844px;top:1212px;text-align:center;color:var(--white);font-size:14px;line-height:30px}

/* services */
.section-title{left:0;width:1200px;text-align:center;font-size:40px;color:var(--ink)}
.section-title span{color:var(--blue)}
.svc{font-size:15px;line-height:22px;color:var(--ink);font-weight:500}
.svc.left{text-align:right}
.center-badge{left:427px;top:1623px;width:346px;height:330px;display:flex;flex-direction:column;align-items:center;justify-content:center;gap:18px}
.center-badge .disc{width:150px;height:150px;border-radius:50%;background:var(--blue)}
.center-badge .name{font-weight:700;font-size:26px;color:var(--ink)}

/* maintenance */
.maint-title{left:171px;top:2210px;font-size:32px;line-height:52px;color:var(--white)}
.maint-copy{left:171px;top:2336px;width:406px;font-size:13px;line-height:27px;color:var(--white);text-align:justify}
.btn{left:171px;top:2554px;width:114px;height:56px;background:var(--blue);color:var(--white);font-family:"Audiowide",sans-serif;font-size:13px;display:flex;align-items:center;justify-content:center;text-transform:uppercase}
.maint-photo{left:598px;top:2024px;width:602px;height:753px;clip-path:polygon(0 7%,100% 0,100% 100%,0 90%);
  background:
    radial-gradient(ellipse 130px 90px at 300px 90px,#f2c318 0%,rgba(242,195,24,0) 100%),
    radial-gradient(ellipse 150px 100px at 470px 190px,#f4f5f6 0%,rgba(244,245,246,0) 100%),
    radial-gradient(ellipse 110px 220px at 430px 540px,#f08a2a 0%,rgba(240,138,42,0) 100%),
    radial-gradient(ellipse 200px 160px at 230px 470px,#27324a 0%,rgba(39,50,74,0) 100%),
    linear-gradient(135deg,#9aa8b4 0%,#6f8192 45%,#44566a 75%,#2f3b4c 100%)}

/* projects */
.proj-copy{left:180px;width:840px;top:2893px;text-align:center;font-size:12.5px;line-height:25px}
.gallery{left:0;top:2988px;width:1200px;height:445px;display:grid;grid-template-columns:repeat(4,1fr);grid-template-rows:1fr 1fr}
.ph-1{background:radial-gradient(ellipse 60px 40px at 130px 40px,#f2c318,rgba(242,195,24,0)),radial-gradient(ellipse 70px 60px at 230px 170px,#ef8a2c,rgba(239,138,44,0)),linear-gradient(135deg,#8d9dac,#3c4d62)}
.ph-2{background:radial-gradient(ellipse 120px 60px at 120px 110px,#6d8896,rgba(109,136,150,0)),linear-gradient(135deg,#3a3f44,#1c2024)}
.ph-3{background:radial-gradient(ellipse 40px 90px at 200px 130px,#c8312a,rgba(200,49,42,0)),radial-gradient(ellipse 70px 80px at 80px 150px,#3a5ea8,rgba(58,94,168,0)),linear-gradient(135deg,#e3e5e8,#9aa3ab)}
.ph-4{background:radial-gradient(ellipse 120px 80px at 150px 110px,#b7d7df,rgba(183,215,223,0)),linear-gradient(135deg,#3f5968,#7d9eac)}
.ph-5{background:radial-gradient(ellipse 70px 100px at 90px 150px,#ef8a2c,rgba(239,138,44,0)),linear-gradient(135deg,#eceae6,#b9b3aa)}
.ph-6{background:radial-gradient(ellipse 120px 80px at 150px 110px,#86b8cc,rgba(134,184,204,0)),linear-gradient(135deg,#2b4456,#1a2a36)}
.ph-7{background:radial-gradient(ellipse 80px 100px at 90px 110px,#d7dde2,rgba(215,221,226,0)),linear-gradient(135deg,#a9b1b7,#55616d)}
.ph-8{background:radial-gradient(ellipse 50px 40px at 250px 70px,#f2c318,rgba(242,195,24,0)),radial-gradient(ellipse 110px 90px at 150px 160px,#3a4350,rgba(58,67,80,0)),linear-gradient(135deg,#f2f3f4,#c5cbd0)}

/* features */
.feature h3{font-weight:400;font-size:25px;line-height:34px}
.feature h3 b{font-weight:500}
.feature p{font-size:13px;line-height:24px;margin-top:12px}

/* footer */
.foot-brand{left:173px;top:3952px;display:flex;align-items:center;gap:14px}
.foot-brand .mark{width:40px;height:40px;border-radius:50%;background:var(--white)}
.foot-brand .name{font-weight:700;font-size:30px;color:var(--white)}
.foot-head{font-size:16px;font-weight:500;color:var(--white)}
.foot-list{list-style:none;font-size:13px;color:var(--white);line-height:28.5px}
.rule{left:173px;top:4150px;width:854px;height:1px;background:#bbb}
.copy{font-size:13px;color:var(--white)}
</style>
</head>
<body>

<!-- hero -->
<div class="abs hero-art" role="img" aria-label="Hero photograph: white hard hat, wooden model house, tape measure, drafting tools and rolled plans in front of a line drawing of city buildings"></div>
<svg class="abs" style="left:0;top:900px" width="1200" height="520" viewBox="0 0 1200 520">
  <polygon points="0,20 600,115 1200,20 1200,514 0,514" fill="var(--blue)"/>
</svg>

<header>
  <div class="abs brand"><div class="brand-mark"></div><div class="brand-name">Corrick &amp; Associates</div></div>
  <nav class="abs nav">
    <a class="active" href="#">HOME</a><a href="#">ABOUT US</a><a href="#">SERVICES</a><a href="#">BLOG</a><a href="#">CONTACT US</a>
  </nav>
</header>

<h1 class="abs display hero-title">Corrick</h1>
<div class="abs display hero-sub">Associates</div>

<!-- about -->
<h2 class="abs display about-title">About Us</h2>
<p class="abs about-copy">Corrick &amp; Associates is specialised manufacturing engineering support organisation that can provide fast, nimble, and flexible services. We have a proven track record in delivering tangible outcomes in process design and fit-out, project management, manufacturing process and maintenance design and execution. Our specialist focus in food manufacturing across a range of sectors allows our team to deliver real benefits to performance and recognition of the clients investment.</p>

<!-- services -->
<h2 class="abs display section-title" style="top:1505px">Our <span>Services</span></h2>

<div class="abs center-badge"><div class="disc"></div><div class="name">Corrick &amp; Associates</div></div>

<div class="abs svc left" style="right:870px;top:1674px">Process &amp; Facilities<br>Design</div>
<div class="abs svc left" style="right:870px;top:1749px">Project<br>Management</div>
<div class="abs svc left" style="right:870px;top:1823px">Major Equipment and<br>Services Installation</div>
<div class="abs svc left" style="right:830px;top:1898px">Engineering &amp;<br>Maintenance Management</div>

<div class="abs svc" style="left:869px;top:1674px">Maintenance<br>Execution</div>
<div class="abs svc" style="left:869px;top:1749px">Manufacturing<br>Performance Measurement</div>
<div class="abs svc" style="left:869px;top:1823px">Vision Inspection<br>Systems</div>
<div class="abs svc" style="left:826px;top:1898px">Acquisition Due<br>Diligence</div>

<svg class="abs" style="left:0;top:0" width="1200" height="2000" viewBox="0 0 1200 2000" fill="none" stroke="var(--ink)" stroke-width="2">
  <rect x="350" y="1678" width="38" height="26" rx="2"/><line x1="362" y1="1712" x2="376" y2="1712"/><circle cx="384" cy="1680" r="6"/>
  <rect x="353" y="1752" width="30" height="38" rx="3"/><text x="361" y="1780" font-size="20" fill="var(--ink)" stroke="none" font-family="Roboto">$</text>
  <rect x="350" y="1828" width="36" height="26" rx="2"/><circle cx="384" cy="1852" r="7"/>
  <circle cx="407" cy="1906" r="9"/><path d="M392 1936 q15 -22 30 0"/><line x1="398" y1="1900" x2="416" y2="1900"/>
  <circle cx="826" cy="1696" r="18"/><circle cx="826" cy="1696" r="7"/>
  <rect x="808" y="1752" width="28" height="36" rx="2"/><circle cx="836" cy="1784" r="9"/><line x1="814" y1="1762" x2="828" y2="1762"/>
  <circle cx="826" cy="1848" r="18"/><circle cx="826" cy="1848" r="10"/><circle cx="826" cy="1848" r="3"/><line x1="826" y1="1848" x2="844" y2="1830"/>
  <rect x="773" y="1902" width="28" height="36" rx="2"/><circle cx="802" cy="1932" r="8"/><line x1="779" y1="1912" x2="794" y2="1912"/>
</svg>

<!-- maintenance & reliability -->
<svg class="abs" style="left:0;top:2020px" width="1200" height="770" viewBox="0 0 1200 770">
  <polygon points="0,32 598,131 598,630 0,729" fill="var(--ink)"/>
</svg>
<div class="abs maint-photo" role="img" aria-label="Photograph of two engineers in hard hats reviewing a tablet in a plant"></div>
<h2 class="abs display maint-title">Maintenance and<br>Reliability</h2>
<p class="abs maint-copy">Nam libero tempore, cum soluta nobis est eligendi optio cumque nihil impedit quo minus id quod maxime placeat facere possimus, omnis vo luptas assumenda est, omnis dolor repellendus. Temporibus autem qui busdam et aut officiis debitis aut rerum necessitatibus saepe eveniet ut et voluptates repudiandae sint et molestiae non recusandae. Itaque earum rerum hic tenetur a sapiente delectus, ut aut reiciendis voluptati bus maiores alias consequatur.</p>
<div class="abs btn">Read More</div>

<!-- projects -->
<h2 class="abs display section-title" style="top:2830px">Our <span>Projects</span></h2>
<p class="abs proj-copy">Nam libero tempore, cum soluta nobis est eligendi optio cumque nihil impedit quo minus id quod maxime placeat facere possimus omnis voluptas assumenda est repellendus.</p>
<div class="abs gallery">
  <div class="ph-1" role="img" aria-label="Project photo: engineers with tablet on site"></div>
  <div class="ph-2" role="img" aria-label="Project photo: engineer at computer monitors"></div>
  <div class="ph-3" role="img" aria-label="Project photo: engineers inspecting plant machinery"></div>
  <div class="ph-4" role="img" aria-label="Project photo: engineer with digital overlay"></div>
  <div class="ph-5" role="img" aria-label="Project photo: engineer with tablet in safety vest"></div>
  <div class="ph-6" role="img" aria-label="Project photo: technology network overlay"></div>
  <div class="ph-7" role="img" aria-label="Project photo: engineers at control panel"></div>
  <div class="ph-8" role="img" aria-label="Project photo: team meeting on factory floor"></div>
</div>

<!-- features & footer background -->
<div class="abs" style="left:0;top:3494px;width:1200px;height:211px;background:var(--sky)"></div>
<div class="abs" style="left:0;top:3705px;width:1200px;height:541px;background:var(--ink)"></div>
<svg class="abs" style="left:397px;top:3494px" width="406" height="306" viewBox="0 0 406 306">
  <polygon points="0,0 406,0 406,211 203,305 0,211" fill="var(--blue)"/>
</svg>

<svg class="abs" style="left:0;top:3540px" width="1200" height="80" viewBox="0 0 1200 80" fill="none" stroke-width="2.5">
  <g stroke="var(--ink)"><rect x="36" y="10" width="40" height="28" rx="3"/><rect x="54" y="24" width="50" height="34" rx="3" fill="var(--sky)"/><circle cx="68" cy="41" r="2.5" fill="var(--ink)"/><circle cx="79" cy="41" r="2.5" fill="var(--ink)"/><circle cx="90" cy="41" r="2.5" fill="var(--ink)"/></g>
  <g stroke="var(--white)"><path d="M438 22 q-8 18 8 34 q14 12 30 6 l-4-10 -10 2 q-10-8-12-20 l8-6 -6-10z"/><rect x="462" y="8" width="34" height="38" rx="4"/><circle cx="479" cy="22" r="6"/></g>
  <g stroke="var(--ink)"><path d="M843 32 l25 -10 25 10 -25 10z"/><path d="M843 32 v26 l25 10 25-10 v-26"/><line x1="868" y1="42" x2="868" y2="68"/><line x1="868" y1="2" x2="868" y2="20"/><path d="M862 14 l6 6 6-6"/></g>
</svg>

<div class="abs feature" style="left:122px;top:3551px;width:260px;color:var(--ink)"><h3>Get your<br><b>Clarifications</b></h3><p>Using our 24/7 knowledgebase, forum &amp; comments get clarified.</p></div>
<div class="abs feature" style="left:524px;top:3551px;width:260px;color:var(--white)"><h3>Legendary<br><b>Support With Us</b></h3><p>Get your doubts cleared using our email support, phone or knowledgebase.</p></div>
<div class="abs feature" style="left:920px;top:3551px;width:260px;color:var(--ink)"><h3>Maintenance<br><b>Packages Available</b></h3><p>We offer annual maintenance packages for different needs.</p></div>

<!-- footer -->
<footer>
  <div class="abs foot-brand"><div class="mark"></div><div class="name">Trivolt Engineering</div></div>
  <div class="abs foot-head" style="left:575px;top:3893px">Useful Links</div>
  <ul class="abs foot-list" style="left:575px;top:3928px"><li>Home</li><li>About Us</li><li>Services</li><li>Blog</li><li>Projects</li></ul>
  <ul class="abs foot-list" style="left:689px;top:3928px"><li>Careers</li><li>Legal Support</li><li>Contact Us</li></ul>
  <div class="abs foot-head" style="left:824px;top:3893px">Contact Us</div>
  <ul class="abs foot-list" style="left:824px;top:3928px">
    <li>48 Harlow Lane, Brookvale,</li><li>MD 20900</li><li style="margin-top:10px">(555) 014-2721</li><li>(555) 019-1352</li><li style="margin-top:10px">info@corrickassociates.com</li>
  </ul>
  <div class="abs rule"></div>
  <div class="abs copy" style="left:0;width:1200px;top:4186px;text-align:center">Copyrights @ 2021 Corrick &amp; Associates. All Rights Reserved.</div>
  <div class="abs copy" style="left:1087px;top:4186px">C20</div>
</footer>

</body>
</html>
```